Startup online payment business - Sporting / Golf, Swift Tee payment

Background:
Our business name is "Swift Tee" we provide online payments for golfing services via our website. We currently have a logo used on our website. No other design style has been developed. Our aim is to remove cash payments for service at golf clubs.

Our Key Values:
Quick and easy
Formal and polite
Fun with professional boundary
Mate-ship relationships
100% online digital

What we want from you:
Marketing design to be used on posters and stickers in a retail setting to direct customers to our online payment Chanel.
Design must incorporate attached logo, URL swifttee.com.au and our key values can act as a guide the type of design. We have used color Hex#007672 for logo background. We are open to use other colors.

Target Market(s)

Golf clubs and golf players

Industry/Entity Type

Golf Course

Font styles to use
Sans Serif

Requirements
Must have
• Directions to online payment via URL: swifttee.com.au
Nice to have
• We like the idea of the slogan: No Cash - No worries. Have attached home screen that will be available from URL link. Consideration if using mobile phone in image. Push the online payment and steps 1. Visit swifttee.com 2. Select club 3. Confirm payment
Should not have
• Cartoons

```html
<!DOCTYPE html>
<html lang="en">
<head>
<meta charset="utf-8">
<title>Swift Tee – No Cash No Worries</title>
<link rel="stylesheet" href="https://fonts.googleapis.com/css2?family=Jost:wght@400;500;700;800&display=swap">
<style>
  :root {
    --teal: #007672;
    --teal-dark: #005f5c;
    --leaf: #a9d48c;
    --sky-top: #e6eeee;
    --sky-mid: #c9f0f8;
    --sky-low: #9fe3f2;
    --tree: #4f8a45;
    --ink: #0b0b0b;
    --white: #ffffff;
    --stage: #e9efee;
  }
  * { margin: 0; padding: 0; box-sizing: border-box; }
  html, body { width: 1200px; height: 675px; overflow: hidden; background: var(--stage); }
  .flyer {
    position: relative;
    width: 1200px;
    height: 675px;
    overflow: hidden;
    font-family: "Jost", sans-serif;
    background: linear-gradient(180deg, var(--sky-top) 0%, var(--sky-mid) 45%, var(--sky-low) 62%, var(--tree) 100%);
  }
  .hero-photo {
    position: absolute;
    left: 0; top: 0;
    width: 620px; height: 420px;
    background: radial-gradient(ellipse at 45% 45%, #7cc6ea 0%, #9fd6ee 35%, rgba(200,235,245,0) 70%);
  }
  .tree-line {
    position: absolute;
    left: 0; top: 300px;
    width: 1200px; height: 120px;
    background: linear-gradient(180deg, rgba(79,138,69,0) 0%, rgba(79,138,69,0.75) 60%, var(--tree) 100%);
  }
  .headline {
    position: absolute;
    right: 40px; top: 30px;
    text-align: right;
    color: var(--ink);
    font-weight: 800;
    line-height: 0.95;
    letter-spacing: 1px;
  }
  .headline .line-one { display: block; font-size: 118px; }
  .headline .line-two { display: block; font-size: 74px; }
  .phone {
    position: absolute;
    left: 690px; top: 250px;
    width: 250px; height: 140px;
    border: 7px solid #141414;
    border-radius: 24px;
    background: var(--teal);
    color: var(--white);
    display: flex;
    align-items: center;
    justify-content: space-around;
    padding: 0 18px;
    z-index: 3;
  }
  .phone-brand { font-size: 24px; font-weight: 700; letter-spacing: 1px; }
  .phone-tagline { font-size: 17px; font-weight: 700; line-height: 1.05; text-align: center; }
  .info-band {
    position: absolute;
    left: 0; top: 405px;
    width: 1200px; height: 270px;
    background: linear-gradient(180deg, var(--teal) 0%, var(--teal-dark) 100%);
    border-top: 5px solid var(--leaf);
  }
  .intro-box {
    position: absolute;
    left: 0; top: 355px;
    width: 470px;
    padding: 12px 22px 14px 30px;
    background: var(--white);
    border-radius: 0 0 22px 0;
    color: var(--teal);
    font-size: 18px;
    font-weight: 700;
    line-height: 1.15;
    z-index: 2;
  }
  .values {
    position: absolute;
    left: 36px; top: 450px;
    list-style: none;
    color: var(--white);
    font-size: 24px;
    line-height: 36px;
    z-index: 2;
  }
  .values li { display: flex; align-items: center; gap: 8px; }
  .values svg { width: 22px; height: 22px; flex: none; }
  .brand {
    position: absolute;
    left: 620px; top: 455px;
    color: var(--white);
    font-size: 64px;
    font-weight: 700;
    letter-spacing: 3px;
    z-index: 2;
  }
  .visit {
    position: absolute;
    left: 520px; top: 585px;
    color: var(--white);
    font-size: 34px;
    font-weight: 500;
    z-index: 2;
  }
</style>
</head>
<body>
<main class="flyer">
  <div class="hero-photo" role="img" aria-label="Photo of a cheering golfer in a blue polo and cap holding a club on the course"></div>
  <div class="tree-line" role="img" aria-label="Blurred tree line of the golf course"></div>

  <h1 class="headline">
    <span class="line-one">NO CASH</span>
    <span class="line-two">NO WORRIES</span>
  </h1>

  <div class="phone">
    <span class="phone-brand">SWIFT TEE</span>
    <span class="phone-tagline">Mobile<br>Payments<br>Method</span>
  </div>

  <section class="info-band"></section>

  <p class="intro-box">Swift Tee is here to support Golf Clubs embrace new strategies for success in a rapidly changing world.</p>

  <ul class="values">
    <li><svg viewBox="0 0 24 24"><path d="M3 13l6 6L21 5" fill="none" stroke="#ffffff" stroke-width="3" stroke-linecap="round" stroke-linejoin="round"/></svg>Quick and easy</li>
    <li><svg viewBox="0 0 24 24"><path d="M3 13l6 6L21 5" fill="none" stroke="#ffffff" stroke-width="3" stroke-linecap="round" stroke-linejoin="round"/></svg>Formal and polite</li>
    <li><svg viewBox="0 0 24 24"><path d="M3 13l6 6L21 5" fill="none" stroke="#ffffff" stroke-width="3" stroke-linecap="round" stroke-linejoin="round"/></svg>Fun with professional boundary</li>
    <li><svg viewBox="0 0 24 24"><path d="M3 13l6 6L21 5" fill="none" stroke="#ffffff" stroke-width="3" stroke-linecap="round" stroke-linejoin="round"/></svg>Mate-ship relationships</li>
    <li><svg viewBox="0 0 24 24"><path d="M3 13l6 6L21 5" fill="none" stroke="#ffffff" stroke-width="3" stroke-linecap="round" stroke-linejoin="round"/></svg>100% online digital</li>
  </ul>

  <div class="brand">SWIFT TEE</div>
  <p class="visit">Visit us at: swifttee.com.au</p>
</main>
</body>
</html>
```